Header for website Size is 1000px x 120px
I have CS5 so will need the source files photoshop, illustrator etc, so I can change text and photos.
Photos attached, includes example header and screenshot of eg site
Brief:
I need a website header for golfers where I can change the photos and their name.
The header needs to have these things.
- pictures of the golfer (use from pics attached)
- Their name
- Also under there name is smaller text I need a line of text you can just say "Offical Website" in your e.g to me
so for example you should have
Dale Forsythe
Offical Website
And some photos that are blended with some nice golf background or some grass or other ideas that you come up with that will look better than mine I'm sure :)
Size is 1000px x 120px
It needs to look professional and blend in nicely. I don't mind how many photos are used maybe 1-4?
The text needs to look professional too but not boring.
The header you create will be used on a website for a Professional Golfer (tour pro) their job is golf, their website needs to showcase them and promote them as best as possible.
As I said above I will need to swap photos easily and edit the text so will need the source files.
So a important point here. I guess there is no need to blend or do anything to the photos you add as I will actually need to change the photos and just need a simple template that I can swap photos and edit their name.
Ultimately I would like 3 versions of the header done and source files for all 3 so I can give them(the golfers) a choice of header type.
See how you go.
Remember that the header must have the ability for me to easily swap images and of course change the text.
My goal is to use the same header for each golfer but obviously with their images and their name.
I have CS5 so will need the source files photoshop, illustrator etc
2 example headers are attached to show you my attempts :) Please do something better.
I don't want any flash.

```html
<!DOCTYPE html>
<html lang="en">
<head>
<meta charset="utf-8">
<title>Dale Forsythe – Header</title>
<link rel="stylesheet" href="https://fonts.googleapis.com/css2?family=Nunito:wght@700;900&display=swap">
<style>
  :root {
    --sky-top: #6f9fc4;
    --sky-low: #b9cbd6;
    --hills: #7f8f8a;
    --grass-far: #4f7a3a;
    --grass-near: #2f5a22;
    --night: #0b0c08;
    --night-green: #1e2a14;
    --turf-dark: #2a3d18;
    --turf-mid: #41582a;
    --turf-light: #6f8a45;
    --sand: #8fa256;
    --silver-hi: #ffffff;
    --silver-lo: #a9adb2;
    --blue-hi: #4aa6ff;
    --blue-lo: #0a4fb8;
    --tagline: #e6ecef;
    --shadow: rgba(0, 0, 0, 0.55);
  }
  * { margin: 0; padding: 0; box-sizing: border-box; }
  html, body { width: 1200px; height: 144px; overflow: hidden; background: #000; }

  .site-header {
    position: relative;
    width: 1200px;
    height: 144px;
    overflow: hidden;
  }

  .scenery {
    position: absolute; left: 0; top: 0; width: 570px; height: 144px;
    background:
      linear-gradient(180deg, transparent 0 34%, var(--hills) 40%, var(--grass-far) 52%, var(--grass-near) 100%),
      linear-gradient(180deg, var(--sky-top) 0%, var(--sky-low) 40%);
    filter: blur(2px);
  }

  .photo { position: absolute; top: 0; height: 144px; }
  .photo--swing {
    left: 558px; width: 240px;
    background: linear-gradient(90deg, var(--night), #141510 60%, var(--night-green));
  }
  .photo--portrait {
    left: 792px; width: 196px;
    background: linear-gradient(90deg, var(--turf-dark), #33471f 50%, var(--turf-mid));
  }
  .photo--bunker {
    left: 984px; width: 216px;
    background: linear-gradient(160deg, var(--turf-light), var(--sand) 50%, #5d7a34);
  }

  .identity {
    position: absolute;
    left: 28px;
    top: 34px;
    font-family: "Nunito", "Arial Rounded MT Bold", sans-serif;
  }
  .golfer-name {
    font-weight: 900;
    font-size: 76px;
    line-height: 1;
    letter-spacing: -0.5px;
    white-space: nowrap;
    filter: drop-shadow(2px 3px 2px var(--shadow));
  }
  .golfer-name__first,
  .golfer-name__last {
    -webkit-background-clip: text;
    background-clip: text;
    color: transparent;
  }
  .golfer-name__first {
    background-image: linear-gradient(180deg, var(--silver-hi) 20%, var(--silver-lo) 95%);
  }
  .golfer-name__last {
    margin-left: 8px;
    background-image: linear-gradient(180deg, var(--blue-hi) 10%, var(--blue-lo) 90%);
  }
  .tagline {
    margin-top: 2px;
    margin-left: 4px;
    font-weight: 700;
    font-size: 15px;
    letter-spacing: 3px;
    text-transform: uppercase;
    color: var(--tagline);
    text-shadow: 1px 1px 2px var(--shadow);
  }
</style>
</head>
<body>
  <header class="site-header">
    <div class="scenery" role="img" aria-label="Softly blurred golf course with blue sky, distant hills and green fairway"></div>
    <div class="photo photo--swing" role="img" aria-label="Photo of the golfer following through a swing against a dark background"></div>
    <div class="photo photo--portrait" role="img" aria-label="Close portrait photo of the golfer on the course"></div>
    <div class="photo photo--bunker" role="img" aria-label="Photo of the golfer playing a shot out of a grassy bunker"></div>
    <div class="identity">
      <h1 class="golfer-name">
        <span class="golfer-name__first">Dale</span><span class="golfer-name__last">Forsythe</span>
      </h1>
      <p class="tagline">Official Website</p>
    </div>
  </header>
</body>
</html>
```